Australia-Wide Industry Leader Bookkeeping Business Website Design Required

We need a website designed for our 10 year old bookkeeping business, Barwick & Lund. Barwick & Lund has been servicing the local & interstate communities of Australia, providing first-class BAS & Bookkeeping services with a personal touch unmatched by anyone else in the county.

What began 10 years ago as a small business focusing on family, friends and the local community, it has since grown into a well respected business with 95% of their business based solely on word of mouth and personal referrals from around Australia.

We would like to see designs that incorporate our existing brand/logo. The colours to be used on the website should be colours that work well with our logo. The design should communicate maturity, trust and confidence with a Web 2.0 look and feel.

We have produced mockups of the entire website as well as assets used in the mockups. Please reference the attached files. The mockups are an example of all the design elements that we want on each page. Designers are encouraged to use the mockups as a guideline only and for designers to use their own creativity.
Updates

This message is for new graphic designers who are considering commencing work on this project. Thank you for expressing an interest in our project. We would like to inform you that this project is close to completion as we have a number designs under very serious consideration.

We are currently in a position where we are disinterested providing feedback to improve on new designs submitted. We will provide feedback to improve new designs only if the submitted designs are very close to what we want for our website, and will only require 1 or 2 revision rounds to refine before the project completion date we will not work with designers to refine their newly submitted designs.

We feel that it is important for all designers to know the above information as we feel that your time and effort may be better spent working on another project.

Thank you for your understanding.

A big thank you for all the designs submitted. We are now in the process of selecting a design. Please be patient during this process. Thank you.

Target Market(s)

Busy Business Owners

Industry/Entity Type

Small Business

Requirements
Must have
• We require a rectangular "slide show" type feature to serve as a "teaser" to arouse the emotions of our website visitors. Each slide asks a specific question. The questions are:

- Is your paperwork in a mess?
- Do you need to get organised for the end of financial year?
- Are you sick & tired of endless amounts of paperwork & BASs?
- Do you feel frustrated & annoyed because you know your books need to be done?
- Do you lack the time & patience to get your paperwork done?
- Do you wish you had more time to do the things you enjoy doing?
- Contact Barwick & Lund today and we will transform your chaos into order.

Underneath the slide show will be a button to "Call Barwick & Lund Now - 03 5550 1827".

```html
<!DOCTYPE html>
<html lang="en">
<head>
<meta charset="utf-8">
<title>Barwick &amp; Lund – BAS &amp; Bookkeeping</title>
<link rel="stylesheet" href="https://fonts.googleapis.com/css2?family=Cabin:wght@400;500;600&family=Cabin+Condensed:wght@400&display=swap">
<style>
:root{
  --red:#9b0d14;
  --red-dark:#7a0a10;
  --ink:#222;
  --body:#4a4a4a;
  --tick:#7cae2a;
  --page:#e2e2e2;
  --panel:#ffffff;
  --line:#cfcfcf;
  --footer:#9a9a9a;
}
*{box-sizing:border-box;margin:0;padding:0}
html,body{width:816px;height:1200px;overflow:hidden}
body{position:relative;font-family:"Cabin",sans-serif;color:var(--body);background:var(--page)}
.abs{position:absolute}
.topbar{left:0;top:0;width:816px;height:3px;background:var(--red)}
.header{left:0;top:3px;width:816px;height:143px;background:linear-gradient(#e6e6e6,#fafafa 50%,#fff);border-bottom:1px solid #d4d4d4}
.brand{left:76px;top:34px;display:flex;align-items:center;gap:8px;font-size:27px;font-weight:500;color:var(--red)}
.brand i{display:block;width:14px;height:14px;background:var(--red)}
.nav{left:324px;top:41px;display:flex;font-size:9.2px;color:var(--ink)}
.nav a{color:inherit;text-decoration:none;padding:4px 8px;border-radius:2px}
.nav a.active{background:var(--red);color:#fff}
.intro{left:75px;top:94px;width:660px;font-size:12px;line-height:16px;color:var(--ink)}
.hero{left:0;top:146px;width:816px;height:260px;background:linear-gradient(100deg,#fdfdfd 40%,#f1f1f1);overflow:hidden}
.hero-swoosh{left:0;top:0}
.hero-photo{left:424px;top:0;width:392px;height:260px;background:linear-gradient(110deg,#f2f2f2 0%,#dfe3e8 30%,#c9ccd3 60%,#eceef1 100%)}
.hero-title{left:81px;top:73px;font-size:22.5px;line-height:25px;color:var(--red);font-weight:500}
.call-btn{left:78px;top:139px;width:130px;height:32px;border-radius:16px;background:linear-gradient(#f2f8fc,#cfe2ef);box-shadow:0 1px 2px rgba(0,0,0,.2);border:2px solid #fff;display:flex;align-items:center;padding-left:12px;font-family:"Cabin Condensed",sans-serif;font-size:14px;color:#222}
.call-btn svg{position:absolute;right:10px;top:7px}
.dots{left:88px;top:245px;display:flex;gap:3px}
.dots span{width:8px;height:8px;border-radius:50%;background:#222}
.dots span:first-child{background:var(--red)}
.welcome{left:75px;top:430px;font-size:22px;font-weight:400;color:var(--ink)}
.welcome b{color:var(--red);font-weight:500}
.story{left:75px;top:462px;width:662px;font-size:9.5px;line-height:13.6px;letter-spacing:.4px}
.panel{background:var(--panel);border:1px solid var(--line);border-radius:3px}
.ribbon{height:23px;background:var(--red);color:#fff;font-size:12px;line-height:23px;padding-left:22px;border-radius:3px 3px 3px 0}
.ribbon:after{content:"";position:absolute;left:0;bottom:-6px;border-top:6px solid var(--red-dark);border-left:13px solid transparent}
ul{list-style:none}
.ticks li{position:relative;padding-left:15px;font-size:8.6px;height:15.7px;line-height:12px;color:#3a3a3a}
.ticks li svg{position:absolute;left:0;top:0}
.ticks li.lead{color:var(--red);font-size:9.7px;line-height:13.5px;height:30px}
.dots-list li{font-size:8.4px;height:14.4px;padding-left:8px;position:relative;color:#3a3a3a}
.dots-list li:before{content:"";position:absolute;left:0;top:4px;width:3px;height:3px;border-radius:50%;background:var(--tick)}
.red{color:var(--red)}
.sub{font-size:9.7px}
.quals li{height:24px;font-size:9px}
.map{left:518px;top:669px;width:204px;height:189px;background:radial-gradient(circle at 50% 55%,#8fc94e,#a7d469 55%,#f2f7ea 80%)}
.partners{left:0;top:1084px;width:816px;height:78px;background:linear-gradient(#f5f5f5,#ebebeb)}
.badge{top:8px;background:#cfcfcf}
.footer{left:0;top:1162px;width:816px;height:38px;background:var(--footer);color:#fff;font-size:8.6px}
.footer p{position:absolute;left:268px;top:14px}
.social{position:absolute;top:10px;width:19px;height:19px;border-radius:3px}
</style>
</head>
<body>
<svg width="0" height="0" class="abs"><defs><symbol id="tick" viewBox="0 0 12 12"><path d="M1 6.5 4.5 10 11 2" fill="none" stroke="#7cae2a" stroke-width="2.4" stroke-linecap="round"/></symbol></defs></svg>

<div class="abs topbar"></div>
<header class="abs header"></header>
<div class="abs brand"><i></i>Barwick &amp; Lund</div>
<nav class="abs nav">
  <a class="active">Home</a><a>About Us</a><a>Services</a><a>Testimonials</a><a>Articles</a><a>Endorsements</a><a>Links</a><a>Contact Us</a>
</nav>
<p class="abs intro">For nearly 10 years Barwick &amp; Lund has been servicing the local &amp; interstate communities of Australia, providing first-class BAS &amp; Bookkeeping services with a personal touch unmatched by anyone else in the country</p>

<section class="abs hero">
  <svg class="abs hero-swoosh" width="430" height="260"><path d="M0 150 C120 200 250 240 430 230" stroke="#f1c9cb" stroke-width="14" fill="none" opacity=".6"/><path d="M0 190 C150 230 260 250 400 260" stroke="#f4d8d9" stroke-width="8" fill="none" opacity=".6"/></svg>
  <div class="abs hero-photo" role="img" aria-label="Photo of a relaxed smiling businessman leaning back with hands behind his head"></div>
  <h1 class="abs hero-title">Do you wish you had more time to<br>do the things you enjoy doing?</h1>
  <div class="abs call-btn">Call us today<svg width="16" height="16" viewBox="0 0 16 16"><circle cx="8" cy="8" r="8" fill="#9b0d14"/><path d="M4 8h6M8 5l3 3-3 3" stroke="#fff" stroke-width="1.8" fill="none"/></svg></div>
  <div class="abs dots"><span></span><span></span><span></span><span></span><span></span></div>
</section>

<h2 class="abs welcome">Welcome to <b>Barwick &amp; Lund</b></h2>
<p class="abs story">Having worked for a Certified Accountants firm for numerous years, Sharon Barwick &amp; Sarah Lund become concerned about the consistency of inaccurate books prepared by others in various organisations. As the quality of bookwork declined. The fees seemed to increase. Together they identified a need for a quality bookkeeping service that truly understood what being in business is all about and more importantly.how to correctly &amp; accurately process books according to the laws and requirments set by National Tax Board. They wanted to give people a better alternative- thus Barwick &amp; Lund was born. What began as a samll busines focusing on family. Friends and the local community has since grown into a well respected business with 95% of their business based solely on word of mouth and personal referrals from around Australia</p>

<div class="abs panel" style="left:79px;top:570px;width:396px;height:498px"></div>
<div class="abs ribbon" style="left:66px;top:575px;width:181px">To Summarise</div>
<ul class="abs ticks" style="left:86px;top:610px;width:200px">
  <li><svg width="11" height="11"><use href="#tick"/></svg>Free initial consultation</li>
  <li><svg width="11" height="11"><use href="#tick"/></svg>Registered BAS Agent #41826-003</li>
  <li><svg width="11" height="11"><use href="#tick"/></svg>Bookkeeping</li>
  <li><svg width="11" height="11"><use href="#tick"/></svg>BAS Preparation &amp; Logdgement</li>
  <li><svg width="11" height="11"><use href="#tick"/></svg>Payroll</li>
  <li><svg width="11" height="11"><use href="#tick"/></svg>IAS Preparation &amp; Logdgement</li>
</ul>
<ul class="abs ticks" style="left:290px;top:610px;width:180px">
  <li><svg width="11" height="11"><use href="#tick"/></svg>Superannuation &amp; Workcover</li>
  <li><svg width="11" height="11"><use href="#tick"/></svg>Margin Scheme</li>
  <li><svg width="11" height="11"><use href="#tick"/></svg>Fuel Tax Credits</li>
  <li><svg width="11" height="11"><use href="#tick"/></svg>Offsite &amp; onsite bookkeeping</li>
  <li><svg width="11" height="11"><use href="#tick"/></svg>Bookwell Software &amp; Training</li>
  <li><svg width="11" height="11"><use href="#tick"/></svg>Australia wide</li>
</ul>
<p class="abs red sub" style="left:90px;top:713px">What makes Barwick &amp; Lund different from other Bookkeepers</p>
<ul class="abs ticks" style="left:86px;top:740px;width:380px">
  <li><svg width="11" height="11"><use href="#tick"/></svg>We guarantee the quality of our work</li>
  <li><svg width="11" height="11"><use href="#tick"/></svg>We have ovaer 35 years of experiencee</li>
  <li><svg width="11" height="11"><use href="#tick"/></svg>We have owned &amp; operated businesses for 35 years</li>
  <li><svg width="11" height="11"><use href="#tick"/></svg>The Barwick &amp; Lund team are investors &amp; traders</li>
  <li><svg width="11" height="11"><use href="#tick"/></svg>Extensive business network for your benefit</li>
  <li><svg width="11" height="11"><use href="#tick"/></svg>Backed by a team of accountants</li>
  <li style="height:28px;line-height:13.5px"><svg width="11" height="11"><use href="#tick"/></svg>We work with a team of elite accointants &amp; wealth creation professionals who<br>coach us monthly in the following:</li>
</ul>
<ul class="abs dots-list" style="left:116px;top:875px">
  <li>Asset Protection</li><li>Superannuation &amp; Self Managed Superannuation Funds</li><li>Property Investing</li><li>Tax strategies. tax structures &amp; best tax savings</li>
</ul>
<ul class="abs ticks" style="left:86px;top:938px;width:385px">
  <li class="lead"><svg width="11" height="11"><use href="#tick"/></svg>We understand just how important it is to help lead &amp; guide our clients from making<br>profits to:</li>
</ul>
<ul class="abs dots-list" style="left:116px;top:984px">
  <li>Maximising profits</li><li>Wealth creation</li><li>Tax Minimisation</li><li>Asset protection</li>
</ul>
<p class="abs red sub" style="left:88px;top:1046px">This is something that other bookkeepers just dont do!</p>

<div class="abs panel" style="left:509px;top:573px;width:232px;height:495px"></div>
<div class="abs ribbon" style="left:494px;top:578px;width:182px">Servicing All of Australia</div>
<p class="abs" style="left:517px;top:616px;width:218px;font-size:8.2px;line-height:13.5px">95% of our clients come from client &amp; accountant referrals. We have clients all over Victoria. Queensland, NSW &amp; Western Australia so no matter where you are we can help</p>
<div class="abs map" role="img" aria-label="Map of Australia marking major cities"></div>
<div class="abs ribbon" style="left:494px;top:864px;width:236px;font-size:11px;padding-left:18px">Qualifiactions, Memberships and Partnerships</div>
<ul class="abs ticks quals" style="left:517px;top:903px;width:220px">
  <li><svg width="11" height="11"><use href="#tick"/></svg>Registered National Tax Board BAS Agent</li>
  <li><svg width="11" height="11"><use href="#tick"/></svg>Certificate IV Financial Services</li>
  <li><svg width="11" height="11"><use href="#tick"/></svg>Certificate III Financial Services</li>
  <li><svg width="11" height="11"><use href="#tick"/></svg>Member of Guild of Chartered Bookkeepers</li>
  <li><svg width="11" height="11"><use href="#tick"/></svg>Platium Member of Coastal Bookkeepers Alliance</li>
  <li><svg width="11" height="11"><use href="#tick"/></svg>Ledgerwood Professional Partner</li>
  <li><svg width="11" height="11"><use href="#tick"/></svg>Meridian Tax Circle</li>
</ul>

<section class="abs partners" aria-label="Partner memberships">
  <div class="abs badge" style="left:119px;width:56px;height:63px;border-radius:6px;background:#d9b3b3"></div>
  <div class="abs badge" style="left:258px;top:6px;width:40px;height:40px;transform:rotate(45deg);background:#e8a36f"></div>
  <div class="abs badge" style="left:371px;width:37px;height:61px;background:#2d4f86"></div>
  <div class="abs badge" style="left:475px;top:16px;width:31px;height:31px;border-radius:50%;background:#c94a4a"></div>
  <div class="abs badge" style="left:572px;top:18px;width:138px;height:30px;background:#c7c7c7"></div>
</section>

<footer class="abs footer">
  <span class="social" style="left:78px;background:#6fb6e0"></span>
  <span class="social" style="left:102px;background:#4d69a3"></span>
  <p>The contents of this site are copyright © 2012, Barwick &amp; Lund. All Rights Reserved.</p>
</footer>
</body>
</html>
```